Plumbing Business Card Design

our business is a plumbing business.
we would like to see designs with our LOGO featured and then either purple or black writing with a white back ground
or black back ground with white or purple writing or even a purple card!
one option we would love to see is if you could get the KTW letters away from the white background ( it is currently in a white box as a jpeg )it is currently on and overlay it onto black.
FRONT
KTW image to be displayed on the front, please use the attached picture. ( you can remove the email address and mobile number from the botttom and re write it in different font or in a different place on the front.
Directly under the large KTW we would like the words Copper Linton Plumbing.
could be spread out like this C O P P E R L I N T O N
P L U M B I N G
We really are open to suggestions though!
Also on the front of the card we could like our little catch phrase somewhere Borra's Trusted Plumber

we dont want in plumbing pictures or photos but we are open to swirl across the card or water movement or droplets.

BACK
These services need to be dot pointed or listed on the back
Hot & Cold Water Services
Gas Fitting
Bathroom & Kitchen Renovations
Metal Roofing & Guttering
New Homes & Extensions
Hot Water Service Changeovers
Drainage & Stormwater Works
All General Plumbing & Maitenance

in smaller writing or down the bottom of the card on the back please display write this Lic. No 492318

Contact Information for Business Card

Reid Linton
Mobile: 0427 316 902
email: copperlintonplumbing@mailvane.example
FInd Us on Socialbook Copper Linton Plumbing ( with the f symbol ) either on the front or the back

```html
<!DOCTYPE html>
<html lang="en">
<head>
<meta charset="utf-8">
<title>Copper Linton Plumbing — Business Card</title>
<link rel="stylesheet" href="https://fonts.googleapis.com/css2?family=Open+Sans:wght@400;600;700;800&display=swap">
<style>
  :root {
    --page: #2b2b2d;
    --purple: #6a4fa8;
    --blue: #4a7fcf;
    --ink: #111111;
    --white: #ffffff;
    --photo-dark: #2e2723;
    --photo-mid: #5a4438;
    --font: "Open Sans", Arial, sans-serif;
  }
  * { box-sizing: border-box; margin: 0; padding: 0; }
  html, body { width: 1200px; height: 900px; overflow: hidden; }
  body { background: var(--page); font-family: var(--font); position: relative; }

  .card {
    position: absolute;
    width: 648px;
    height: 360px;
    border-radius: 22px;
    overflow: hidden;
    box-shadow: 0 14px 34px rgba(0,0,0,0.45);
  }
  .card-shapes { position: absolute; inset: 0; width: 100%; height: 100%; }

  /* Back card */
  .card-back { left: 110px; top: 60px; }
  .back-logo {
    position: absolute; top: 22px; right: 110px;
    font-size: 84px; font-weight: 800; letter-spacing: 4px;
    color: var(--blue); line-height: 1;
  }
  .services {
    position: absolute; top: 118px; right: 22px;
    list-style: none; text-align: right; color: var(--white);
    font-size: 14px; line-height: 20px;
  }
  .services li { display: flex; justify-content: flex-end; align-items: center; gap: 10px; }
  .services li::after {
    content: ""; width: 11px; height: 11px; border-radius: 50%; background: var(--white);
  }
  .services .services-title { font-weight: 700; }
  .services .services-title::after { visibility: hidden; }
  .services .no-dot::after { visibility: hidden; }
  .back-footer {
    position: absolute; left: 30px; bottom: 26px;
    color: var(--white); font-size: 15px; line-height: 22px;
  }
  .social-line { display: flex; align-items: center; gap: 8px; }
  .social-dot { width: 10px; height: 10px; border-radius: 50%; background: var(--white); }

  /* Front card */
  .card-front { left: 442px; top: 480px; background: var(--white); }
  .front-logo { position: absolute; left: 52px; top: 70px; color: var(--blue); }
  .front-logo .mark { font-size: 76px; font-weight: 800; letter-spacing: 4px; line-height: 1; }
  .front-logo .wordmark { font-size: 17px; font-weight: 700; letter-spacing: 5px; line-height: 22px; margin-top: 4px; }
  .front-logo .wordmark-sub { padding-left: 26px; }
  .contact { position: absolute; left: 48px; top: 228px; color: var(--ink); }
  .contact .name { font-size: 27px; font-weight: 800; letter-spacing: 0.5px; margin-bottom: 10px; }
  .contact .line { display: flex; align-items: center; gap: 8px; font-size: 16px; line-height: 24px; }
  .contact svg { width: 14px; height: 14px; fill: none; stroke: var(--blue); stroke-width: 2; }
</style>
</head>
<body>

  <section class="card card-back" aria-label="Card back">
    <svg class="card-shapes" viewBox="0 0 648 360" preserveAspectRatio="none">
      <defs>
        <linearGradient id="photoTone" x1="0" y1="0" x2="1" y2="1">
          <stop offset="0" stop-color="#3b302a"/>
          <stop offset="0.5" stop-color="#5a4438"/>
          <stop offset="1" stop-color="#2e2723"/>
        </linearGradient>
      </defs>
      <rect width="648" height="360" fill="url(#photoTone)" role="img" aria-label="Photo of a plumber clearing a drain in a paved courtyard"/>
      <path d="M0,112 C130,265 320,338 560,360 L0,360 Z" fill="#ffffff"/>
      <path d="M0,130 C130,278 300,345 480,360 L0,360 Z" fill="#6a4fa8"/>
    </svg>
    <div class="back-logo">KTW</div>
    <ul class="services">
      <li class="services-title">SERVICES:</li>
      <li>Hot &amp; Cold Water Services</li>
      <li>Gas Fitting</li>
      <li>Bathroom &amp; Kitchen Renovations</li>
      <li>Metal Roofing &amp; Guttering</li>
      <li>New Homes &amp; Extensions</li>
      <li>Hot Water Service Changeovers</li>
      <li class="no-dot">Drainage &amp; Stormwater Works</li>
      <li class="no-dot">All General Plumbing &amp; Maitenance</li>
    </ul>
    <div class="back-footer">
      <p>Find Us on Socialbook:</p>
      <p class="social-line"><span class="social-dot"></span>Copper Linton Plumbing</p>
      <p>Lic. No 492318</p>
    </div>
  </section>

  <section class="card card-front" aria-label="Card front">
    <svg class="card-shapes" viewBox="0 0 648 360" preserveAspectRatio="none">
      <path d="M548,0 C640,70 650,210 380,360 L648,360 L648,0 Z" fill="#6a4fa8"/>
      <path d="M540,0 C628,72 636,212 372,360" fill="none" stroke="#111111" stroke-width="7"/>
    </svg>
    <div class="front-logo">
      <div class="mark">KTW</div>
      <div class="wordmark">C O P P E R L I N T O N</div>
      <div class="wordmark wordmark-sub">P L U M B I N G</div>
    </div>
    <div class="contact">
      <p class="name">REID LINTON</p>
      <p class="line">
        <svg viewBox="0 0 16 16"><path d="M4 1.5 L6.5 4.5 L5 6.5 C6 8.5 7.5 10 9.5 11 L11.5 9.5 L14.5 12 L12.5 14.5 C6.5 14 2 9.5 1.5 3.5 Z"/></svg>
        0427 316 902
      </p>
      <p class="line">
        <svg viewBox="0 0 16 16"><rect x="1.5" y="3.5" width="13" height="9"/><path d="M1.5 3.5 L8 9 L14.5 3.5"/></svg>
        copperlintonplumbing@mailvane.example
      </p>
    </div>
  </section>

</body>
</html>
```